Book cover for The Quiet Harbor Method to Grow a Fearless Venture

Book cover design for soft cover non-fiction book.

The front cover is what is most important at this stage, I am still gathering the testimonials and book description for the back cover so a rough to be completed later for the back is great.

Title as per above. Held Steady "The Quiet Harbor Method" (to be a series) and "Grow a Fearless Venture" in this book in the series

Also for the front:

Corla Vennick

"The most unusual business book you will read." - Jodi Marquenthal, Author of Founder Tidewalk

Background info:

This work is a blending of the masculine and feminine energies, the practical business skills with a strong focus on the inner game. I am looking for the cover to have a nod to the Dominatrix and a clear message that one can be soft (kind, open hearted) and still be strong and firm in business.

Photo options are in this file https://www.filecrate-share.example/sh/qk41mxw07trbvle/BBFupdmWqYrLs3NxKeei47K5b?dl=0

Size 6" x 9" 179 pgs

Target Market(s)

female entreprenures

Industry/Entity Type

Business

Colors

Designer to choose colors to be used in the design.

Requirements
Must have
• I would like the title to be in a font that is bold and upscale, to contrast the softness fo the image.
• Clear and readable
• Unique look that will stand out
Should not have
• overt Dominatrix images or slant. It is about the energy not the actual.

```html
<!DOCTYPE html>
<html lang="en">
<head>
<meta charset="utf-8">
<title>Held Steady — The Quiet Harbor Method — Book Cover</title>
<link rel="stylesheet" href="https://fonts.googleapis.com/css2?family=Cinzel:wght@600;700;800&family=Roboto:wght@300&display=swap">
<style>
  :root {
    --backdrop: #8f9437;
    --cover-top: #07080b;
    --cover-mid: #1f2a40;
    --cover-bottom: #3f5585;
    --title-white: #ffffff;
    --ink-dark: #111216;
    --photo-light: #ecebe8;
    --photo-skin: #b98c76;
    --photo-red: #c8201c;
  }
  * { margin: 0; padding: 0; box-sizing: border-box; }
  html, body {
    width: 1200px; height: 1200px; overflow: hidden;
    background: var(--backdrop);
  }
  .cover {
    position: absolute;
    left: 241px; top: 91px;
    width: 706px; height: 1037px;
    overflow: hidden;
    background: linear-gradient(180deg, var(--cover-top) 0%, var(--cover-mid) 45%, var(--cover-bottom) 100%);
  }
  .cover-photo {
    position: absolute;
    left: 200px; top: 290px;
    width: 506px; height: 747px;
  }
  .series-title {
    position: absolute;
    left: 53px; top: 76px;
    font-family: "Cinzel", serif;
    font-weight: 700;
    font-size: 74px;
    line-height: 1;
    color: var(--title-white);
    letter-spacing: 2px;
    white-space: nowrap;
  }
  .series-title .initial { font-size: 98px; }
  .series-name {
    position: absolute;
    left: 57px; top: 178px;
    font-family: "Roboto", sans-serif;
    font-weight: 300;
    font-size: 38px;
    color: var(--title-white);
    white-space: nowrap;
  }
  .book-title {
    position: absolute;
    left: 52px; top: 300px;
    font-family: "Roboto", sans-serif;
    font-weight: 300;
    color: var(--title-white);
  }
  .book-title .lead { display: block; font-size: 32px; line-height: 1; margin-bottom: 12px; }
  .book-title .main { display: block; font-size: 62px; line-height: 63px; text-transform: uppercase; }
  .credits {
    position: absolute;
    left: 46px; top: 836px;
    font-family: "Cinzel", serif;
    color: var(--ink-dark);
  }
  .credits .author { font-size: 30px; font-weight: 800; line-height: 1; display: block; letter-spacing: 2px; }
  .credits .quote { font-size: 17px; font-weight: 800; display: block; margin-top: 6px; letter-spacing: 1.5px; }
  .credits .endorser { font-size: 30px; font-weight: 800; line-height: 1; display: block; margin-top: 20px; letter-spacing: 2px; }
  .credits .endorser-role { font-size: 19px; font-weight: 700; display: block; margin-top: 2px; letter-spacing: 1.5px; }
</style>
</head>
<body>
  <div class="cover">
    <svg class="cover-photo" role="img" aria-label="Photo of a businesswoman in a white shirt wearing red boxing gloves in a guard stance" viewBox="0 0 506 747" preserveAspectRatio="none">
      <defs>
        <linearGradient id="photo-tone" x1="0" y1="0" x2="0" y2="1">
          <stop offset="0" stop-color="var(--photo-skin)" stop-opacity="0.15"/>
          <stop offset="0.3" stop-color="var(--photo-skin)" stop-opacity="0.6"/>
          <stop offset="0.55" stop-color="var(--photo-red)" stop-opacity="0.6"/>
          <stop offset="1" stop-color="var(--photo-light)" stop-opacity="0.85"/>
        </linearGradient>
        <linearGradient id="photo-fade" x1="0" y1="0" x2="1" y2="0">
          <stop offset="0" stop-color="#fff" stop-opacity="0"/>
          <stop offset="0.35" stop-color="#fff" stop-opacity="1"/>
          <stop offset="1" stop-color="#fff" stop-opacity="1"/>
        </linearGradient>
        <mask id="photo-mask">
          <rect width="506" height="747" fill="url(#photo-fade)"/>
        </mask>
      </defs>
      <rect width="506" height="747" fill="url(#photo-tone)" mask="url(#photo-mask)"/>
    </svg>

    <div class="series-title"><span class="initial">H</span>ELD STEADY</div>
    <div class="series-name">The Quiet Harbor Method</div>

    <h1 class="book-title">
      <span class="lead">Grow a</span>
      <span class="main">Fearless<br>Venture</span>
    </h1>

    <div class="credits">
      <span class="author">Corla Vennick</span>
      <span class="quote">The most unusual business book you will read.</span>
      <span class="endorser">Jodi Marquenthal</span>
      <span class="endorser-role">Author of Founder Tidewalk</span>
    </div>
  </div>
</body>
</html>
```